TomasTunes poster

We need a poster to promote my live music show for hotels, Im playing for tourists in hotels in Palma de Mallorca, Spain, I would like to see the url of my web site in the poster www.tomastunes.es, in the web site you can see some of my music, thx

```html
<!DOCTYPE html>
<html lang="en">
<head>
<meta charset="utf-8">
<title>TomasTunes poster</title>
<link href="https://fonts.googleapis.com/css2?family=Montserrat:ital,wght@0,300;0,500;0,700;0,800;1,500&family=Lobster&display=swap" rel="stylesheet">
<style>
  :root {
    --page-bg: #b3b3b3;
    --green-top: #7a9e8b;
    --green-mid: #5f8672;
    --green-deep: #34574a;
    --ink: #111111;
    --paper: #ffffff;
    --photo-light: #c9c9c9;
    --photo-dark: #3d3d3d;
  }
  * { box-sizing: border-box; margin: 0; padding: 0; }
  html, body { width: 1200px; height: 900px; overflow: hidden; }
  body {
    background: var(--page-bg);
    font-family: "Montserrat", Arial, sans-serif;
    position: relative;
  }
  .poster {
    position: absolute;
    left: 308px;
    top: 40px;
    width: 584px;
    height: 820px;
    background: linear-gradient(180deg, var(--green-top) 0%, var(--green-mid) 55%, var(--green-deep) 100%);
    box-shadow: 0 6px 18px rgba(0,0,0,0.35);
    color: var(--paper);
    text-align: center;
  }
  .show-circle {
    position: absolute;
    left: 12px;
    top: 23px;
    width: 560px;
    height: 560px;
    border-radius: 50%;
    background: var(--paper);
    padding: 8px;
  }
  .show-circle__inner {
    width: 100%;
    height: 100%;
    border-radius: 50%;
    border: 5px solid var(--ink);
    overflow: hidden;
    position: relative;
    background: var(--paper);
  }
  .brand-name {
    position: absolute;
    top: 62px;
    left: 0;
    right: 0;
    font-weight: 800;
    font-size: 50px;
    color: var(--ink);
    letter-spacing: 1px;
  }
  .stage-photo {
    position: absolute;
    left: 0;
    right: 0;
    top: 170px;
    bottom: 0;
    background: linear-gradient(180deg, var(--paper) 0%, var(--photo-light) 12%, #8a8a8a 40%, var(--photo-dark) 100%);
  }
  .catch-line {
    position: absolute;
    top: 618px;
    left: 0; right: 0;
    font-family: "Lobster", cursive;
    font-size: 36px;
    line-height: 1;
  }
  .venue {
    position: absolute;
    top: 664px;
    left: 0; right: 0;
    font-weight: 800;
    font-size: 35px;
    line-height: 1;
    letter-spacing: 0.5px;
  }
  .show-date {
    position: absolute;
    top: 708px;
    left: 0; right: 0;
    font-weight: 300;
    font-size: 29px;
    line-height: 1;
    letter-spacing: 1px;
  }
  .contact-pill {
    position: absolute;
    top: 749px;
    left: 83px;
    width: 418px;
    height: 31px;
    border-radius: 16px;
    background: var(--ink);
    font-style: italic;
    font-weight: 500;
    font-size: 14px;
    line-height: 31px;
  }
  .site-url {
    position: absolute;
    top: 789px;
    left: 0; right: 0;
    font-size: 13px;
    letter-spacing: 4px;
  }
</style>
</head>
<body>
  <article class="poster">
    <div class="show-circle">
      <div class="show-circle__inner">
        <div class="brand-name">TomasTunes</div>
        <div class="stage-photo" role="img" aria-label="Black and white photo of a guitarist playing seated on a hotel terrace by the harbour, hillside town behind"></div>
      </div>
    </div>
    <p class="catch-line">Catch Me @</p>
    <h1 class="venue">THE NAME OF THE HOTEL</h1>
    <p class="show-date">DD/MM/YEAR</p>
    <p class="contact-pill">For more information Email us : hello@tomastunes.es</p>
    <p class="site-url">www.tomastunes.es</p>
  </article>
</body>
</html>
```